New grafic design homepage www.klimvaro.be
Needs
The homepage design should improve and build on the design of www.dovamex.nl and www.wuntra.be. Following requirements:
1. Functional and visually oriented
2. Icons for "drogen", "verwarming" (5) etc on the website www.klimvaro.be must be used, size could be varied (see attachments for example)
3. Call to action for webshop
4. Call to action for online chat, call me, email me and contact form
5. Online brochure button, search per product section, search for usage
section.
6. Creative design for project references/testimonials section
7. Use www.dovamex as a base for the design..I like this design but would
like to see improvements.
8. Less is more, so please work on an intuitive and functional design
using images.
9. Visible "Why Klimvaro" section with bulletpoint presentation of USP's
10. LOGO text changed to "Shape your comfort"
Company description
Rental business. Company rents out equipment for air quality control such as air conditioners, coolers, heaters, humidifyers, dryers to Belgium customers.
Target group
Target market segments are: construction companies, industry with climate control issues. Owners of shops, server rooms, organizers of events, office buildings. Construction site operators.
Colors, favourites and other requirements
Improve the design of the homepages of www.dovamex.nl and www.wuntra.be using creative ideas to incorporate the requirements.
Use the 5 icons for the 5 product ranges (see attachments)

```html
<!DOCTYPE html>
<html lang="nl">
<head>
<meta charset="utf-8">
<title>Klimvaro – Verhuur | advies | service</title>
<link href="https://fonts.googleapis.com/css2?family=Open+Sans:wght@300;400;600;700&display=swap" rel="stylesheet">
<style>
  :root {
    --orange: #f28a1e;
    --blue: #3b9fd9;
    --ink: #333333;
    --muted: #777777;
    --line: #e2e2e2;
    --hero-top: #e9e9e9;
    --hero-bottom: #fbfbfb;
    --footer: #3b3b3b;
    --footer-deep: #2c2c2c;
    --footer-text: #d8d8d8;
    --white: #ffffff;
  }
  * { margin: 0; padding: 0; box-sizing: border-box; }
  html, body { width: 1200px; height: 800px; overflow: hidden; }
  body { font-family: "Open Sans", Arial, sans-serif; color: var(--ink); background: var(--white); position: relative; }

  /* Header */
  .site-header { position: absolute; left: 0; top: 0; width: 1200px; height: 72px; background: var(--white); border-top: 3px solid #d0d0d0; box-shadow: 0 2px 6px rgba(0,0,0,.12); z-index: 2; }
  .brand { position: absolute; left: 208px; top: 16px; display: flex; align-items: center; gap: 8px; }
  .brand-mark { width: 20px; height: 20px; background: var(--orange); border-radius: 50%; }
  .brand-text { display: flex; flex-direction: column; line-height: 1; }
  .brand-name { font-size: 24px; font-weight: 700; color: #2d2d2d; letter-spacing: .5px; }
  .brand-tagline { font-size: 7px; font-weight: 700; color: #2d2d2d; letter-spacing: 1px; margin-top: 3px; text-transform: uppercase; }
  .main-nav { position: absolute; top: 0; left: 510px; display: flex; height: 69px; }
  .main-nav a { display: block; padding: 28px 15px 0; font-size: 9px; font-weight: 600; color: #555; text-decoration: none; text-transform: uppercase; letter-spacing: .2px; }
  .main-nav a.is-active { color: var(--orange); border-top: 3px solid var(--orange); margin-top: -3px; }

  /* Hero */
  .hero { position: absolute; left: 0; top: 72px; width: 1200px; height: 324px; background: linear-gradient(var(--hero-top), var(--hero-bottom) 55%, var(--white)); }
  .call-box { position: absolute; left: 220px; top: 18px; display: flex; gap: 8px; align-items: center; }
  .call-number { font-size: 12px; font-weight: 600; line-height: 1.1; }
  .call-note { font-size: 8px; color: var(--muted); }
  .welcome { position: absolute; left: 0; width: 1200px; top: 38px; text-align: center; }
  .welcome h1 { font-size: 18px; font-weight: 400; color: #222; line-height: 1.2; }
  .welcome h1 b { font-weight: 700; }
  .welcome .services { font-size: 11px; color: #555; margin-top: 1px; }
  .welcome .intro { font-size: 9px; color: var(--muted); margin-top: 3px; }
  .hero-rule { position: absolute; left: 220px; top: 128px; width: 770px; height: 1px; background: var(--line); }

  .products { position: absolute; left: 200px; top: 110px; width: 800px; height: 210px; display: flex; }
  .product { position: relative; width: 160px; height: 100%; text-align: center; }
  .product + .product::before { content: ""; position: absolute; left: 0; top: 40px; height: 160px; width: 1px; background: var(--line); }
  .product-icon { width: 22px; height: 22px; margin: 0 auto; display: block; }
  .photo-slot { height: 112px; margin-top: 24px; display: flex; align-items: center; justify-content: center; }
  .product-photo { border-radius: 4px; }
  .product-label { margin-top: 16px; font-size: 11px; color: #444; }
  .product-label b { font-weight: 700; color: #333; }
  .product-label em { font-style: normal; color: var(--orange); }

  .orange-rule { position: absolute; left: 0; top: 396px; width: 1200px; height: 2px; background: var(--orange); }

  /* Why & testimonials */
  .why { position: absolute; left: 288px; top: 432px; }
  .section-title { font-size: 17px; font-weight: 600; color: #333; margin-bottom: 10px; }
  .section-title.light { font-weight: 400; }
  .section-title.light b { font-weight: 700; }
  .usp-list { list-style: none; }
  .usp-list li { font-size: 10px; color: #555; line-height: 15.5px; display: flex; align-items: center; gap: 8px; }
  .usp-list svg { width: 9px; height: 9px; flex: none; }
  .testimonials { position: absolute; left: 760px; top: 432px; width: 260px; }
  .quote { margin-bottom: 8px; font-size: 10px; line-height: 14px; color: #555; }
  .quote strong { display: block; color: #333; font-weight: 700; }

  /* Footer */
  .site-footer { position: absolute; left: 0; top: 634px; width: 1200px; height: 136px; background: var(--footer); border-top: 2px solid var(--orange); color: var(--footer-text); font-size: 10px; }
  .footer-col { position: absolute; top: 18px; line-height: 15px; }
  .footer-col h3 { font-size: 13px; color: var(--white); font-weight: 700; line-height: 18px; }
  .footer-col.brand-col { left: 208px; }
  .footer-col.col-2 { left: 364px; top: 38px; }
  .footer-col.col-3 { left: 524px; top: 38px; }
  .contact-col { position: absolute; left: 836px; top: 26px; }
  .contact-item { display: flex; gap: 8px; margin-bottom: 6px; line-height: 12px; }
  .contact-item svg { width: 10px; height: 10px; margin-top: 1px; flex: none; }
  .contact-item b { color: var(--white); display: block; }
  .copyright { position: absolute; left: 0; top: 770px; width: 1200px; height: 30px; background: var(--footer-deep); color: var(--footer-text); font-size: 10px; padding: 8px 0 0 208px; }
</style>
</head>
<body>

<header class="site-header">
  <div class="brand">
    <span class="brand-mark"></span>
    <span class="brand-text">
      <span class="brand-name">KLIMVARO</span>
      <span class="brand-tagline">Shape your comfort</span>
    </span>
  </div>
  <nav class="main-nav">
    <a href="#" class="is-active">Home</a>
    <a href="#">Airconditioning</a>
    <a href="#">Verwarming</a>
    <a href="#">Ventilatie</a>
    <a href="#">Droging</a>
    <a href="#">Bevochtiging</a>
  </nav>
</header>

<section class="hero">
  <div class="call-box">
    <svg width="22" height="22" viewBox="0 0 24 24"><circle cx="12" cy="12" r="11" fill="none" stroke="#444" stroke-width="1.5"/><path d="M8 6.5l2 0 1 3-1.4 1a7 7 0 0 0 3.9 3.9l1-1.4 3 1v2c0 .6-.5 1-1 1A10 10 0 0 1 7 7.5c0-.6.4-1 1-1z" fill="#444"/></svg>
    <div>
      <div class="call-number">0800 31 207</div>
      <div class="call-note">Bel ons voor advies</div>
    </div>
  </div>

  <div class="welcome">
    <h1><b>Welkom</b> bij KLIMVARO</h1>
    <p class="services">Verhuur | advies | service</p>
    <p class="intro">Mobiel klimaatbeheer voor airconditioning, verwarming, ventilatie, droging, bevochtiging.</p>
  </div>

  <div class="hero-rule"></div>

  <div class="products">
    <div class="product">
      <svg class="product-icon" viewBox="0 0 24 24" stroke="var(--blue)" stroke-width="2" stroke-linecap="round" fill="none"><path d="M12 2v20M3.3 7l17.4 10M3.3 17L20.7 7M9.5 3.5L12 6l2.5-2.5M9.5 20.5L12 18l2.5 2.5"/></svg>
      <div class="photo-slot"><div class="product-photo" role="img" aria-label="Mobiele airconditioner" style="width:70px;height:100px;background:linear-gradient(#f4f4f4,#cfd3d6)"></div></div>
      <p class="product-label"><b>Airco</b> <em>huren</em></p>
    </div>
    <div class="product">
      <svg class="product-icon" viewBox="0 0 24 24"><path d="M12 2c3 5 7 8 7 13a7 7 0 0 1-14 0c0-3 2-5 3-6 0 2 1 3 2 3 0-4 0-7 2-10z" fill="var(--blue)"/></svg>
      <div class="photo-slot"><div class="product-photo" role="img" aria-label="Elektrische heater" style="width:86px;height:80px;background:linear-gradient(#4f9fe0,#2a6fb8)"></div></div>
      <p class="product-label"><b>Verwarming</b> <em>huren</em></p>
    </div>
    <div class="product">
      <svg class="product-icon" viewBox="0 0 24 24" fill="var(--blue)"><circle cx="12" cy="12" r="2"/><path d="M12 10c-1-4 0-7 3-7 2 0 2 3-3 7zM14 12c4-1 7 0 7 3 0 2-3 2-7-3zM12 14c1 4 0 7-3 7-2 0-2-3 3-7zM10 12c-4 1-7 0-7-3 0-2 3-2 7 3z"/></svg>
      <div class="photo-slot"><div class="product-photo" role="img" aria-label="Gele ventilator op statief" style="width:86px;height:92px;border-radius:50%;background:radial-gradient(#3a3a3a 30%,#f2cf1d 34%,#d9b20d)"></div></div>
      <p class="product-label"><b>Ventilatie</b> <em>huren</em></p>
    </div>
    <div class="product">
      <svg class="product-icon" viewBox="0 0 24 24" stroke="var(--blue)" stroke-width="2" fill="none" stroke-linecap="round"><path d="M6 3c-2 2 2 4 0 7M12 3c-2 2 2 4 0 7M18 3c-2 2 2 4 0 7M3 15h18v5H3z"/></svg>
      <div class="photo-slot"><div class="product-photo" role="img" aria-label="Bouwdroger" style="width:72px;height:100px;background:linear-gradient(#f0d42a,#c9ad10)"></div></div>
      <p class="product-label"><b>Droging</b> <em>huren</em></p>
    </div>
    <div class="product">
      <svg class="product-icon" viewBox="0 0 24 24" fill="var(--blue)"><circle cx="5" cy="5" r="2"/><circle cx="12" cy="5" r="2"/><circle cx="19" cy="5" r="2"/><circle cx="5" cy="12" r="2"/><circle cx="12" cy="12" r="2"/><circle cx="19" cy="12" r="2"/><circle cx="5" cy="19" r="2"/><circle cx="12" cy="19" r="2"/><circle cx="19" cy="19" r="2"/></svg>
      <div class="photo-slot"><div class="product-photo" role="img" aria-label="Luchtbevochtiger" style="width:90px;height:90px;background:linear-gradient(#e4e6e8,#a9aeb3)"></div></div>
      <p class="product-label"><b>Bevochtiging</b> <em>huren</em></p>
    </div>
  </div>
</section>

<div class="orange-rule"></div>

<section class="why">
  <h2 class="section-title">Waarom KLIMVARO</h2>
  <ul class="usp-list">
    <li><svg viewBox="0 0 10 10"><path d="M1 5l3 3 5-6" stroke="#555" stroke-width="1.8" fill="none"/></svg>Deskundig advies</li>
    <li><svg viewBox="0 0 10 10"><path d="M1 5l3 3 5-6" stroke="#555" stroke-width="1.8" fill="none"/></svg>Snelle 24-uurs levering</li>
    <li><svg viewBox="0 0 10 10"><path d="M1 5l3 3 5-6" stroke="#555" stroke-width="1.8" fill="none"/></svg>Maatwerk kwaliteitsoplossingen</li>
    <li><svg viewBox="0 0 10 10"><path d="M1 5l3 3 5-6" stroke="#555" stroke-width="1.8" fill="none"/></svg>Laagste prijs in België</li>
    <li><svg viewBox="0 0 10 10"><path d="M1 5l3 3 5-6" stroke="#555" stroke-width="1.8" fill="none"/></svg>Al eerder klant? Nog meer korting!</li>
    <li><svg viewBox="0 0 10 10"><path d="M1 5l3 3 5-6" stroke="#555" stroke-width="1.8" fill="none"/></svg>Geen hoge aanschaf en onderhoudskosten</li>
  </ul>
</section>

<section class="testimonials">
  <h2 class="section-title light">Wat <b>klanten</b> zeggen</h2>
  <p class="quote"><strong>John Doe</strong>Lorem ipsum dolor sit amet, consectetur.</p>
  <p class="quote"><strong>Jane Doe</strong>Lorem ipsum dolor sit amet.</p>
  <p class="quote"><strong>Richard Doe</strong>Lorem ipsum dolor sit amet, consectetur.</p>
</section>

<footer class="site-footer">
  <div class="footer-col brand-col">
    <h3>KLIMVARO</h3>
    <div>Over KLIMVARO</div>
    <div>Klantenservice</div>
    <div>FAQ</div>
    <div>Contact</div>
  </div>
  <div class="footer-col col-2">
    <div>Sponsoring Lumo</div>
    <div>Blog</div>
    <div>Smartphone app</div>
  </div>
  <div class="footer-col col-3">
    <div>Disclaimer</div>
    <div>Veiligheid</div>
    <div>Algemene voorwaarden</div>
  </div>
  <div class="contact-col">
    <div class="contact-item">
      <svg viewBox="0 0 10 10"><path d="M1 5L5 1l4 4v4H1z" fill="#fff"/></svg>
      <div><b>Adres</b>Lindenlaan 48, 2000 AB</div>
    </div>
    <div class="contact-item">
      <svg viewBox="0 0 10 10"><path d="M2 1h2l1 2.5-1.2.8a5 5 0 0 0 2 2l.8-1.2L9 6v2c0 .5-.5 1-1 1A7.5 7.5 0 0 1 1 2c0-.5.5-1 1-1z" fill="#fff"/></svg>
      <div><b>Telefoon</b>0800 31 207</div>
    </div>
    <div class="contact-item">
      <svg viewBox="0 0 10 10"><rect x="0.5" y="2" width="9" height="6.5" fill="#fff"/><path d="M0.5 2L5 6l4.5-4" stroke="#3b3b3b" fill="none"/></svg>
      <div><b>Email</b>info@klimvaro.be</div>
    </div>
  </div>
</footer>

<div class="copyright">© Copyright 2014 - klimvaro.be</div>

</body>
</html>
```